Tidewell Care Community Catalogue

I would like an A4 brochure designed consistent with my company branding . This can be seen at www.tidewellcare.com.au . All content is available in document below.

I've also included the brand guidelines document.

Target Market(s)

People in the community suffering from injuries & Disabilities

Industry/Entity Type

Health Service

Font styles to use

Colors
33b8a4
acd037

Requirements
Must have
• Good use of the pictures I've included.
• Brand colours & Fonts
• Consistency with brand look and feel

```html
<!DOCTYPE html>
<html lang="en">
<head>
<meta charset="utf-8">
<title>Tidewell Care Community Catalogue – Pages 4 and 5</title>
<link rel="stylesheet" href="https://fonts.googleapis.com/css2?family=Montserrat:wght@400;500;600;700&display=swap">
<style>
  :root {
    --teal: #33b8a4;
    --teal-soft: #5cc8b0;
    --teal-pale: #c9ece5;
    --green: #acd037;
    --green-pale: #e4f1c4;
    --navy: #1b2a4a;
    --ink: #2c2f36;
    --tab-grey: #7d7d7d;
    --paper: #ffffff;
    --backdrop: #ece9e4;
  }
  * { box-sizing: border-box; margin: 0; padding: 0; }
  html, body { width: 1200px; height: 900px; overflow: hidden; }
  body {
    background: var(--backdrop);
    font-family: "Montserrat", sans-serif;
    color: var(--ink);
    position: relative;
  }
  .page {
    position: absolute;
    top: 72px;
    width: 482px;
    height: 676px;
    background: var(--paper);
    overflow: hidden;
    box-shadow: 0 2px 10px rgba(0,0,0,0.18);
  }
  .page--left { left: 88px; }
  .page--right { left: 631px; }
  .page-decor { position: absolute; inset: 0; width: 482px; height: 676px; }
  .page-frame {
    position: absolute;
    border: 1.3px solid var(--navy);
  }
  .page--left .page-frame { left: 30px; top: 27px; width: 438px; height: 622px; }
  .page--right .page-frame { left: 12px; top: 27px; width: 441px; height: 622px; }
  .page-number {
    position: absolute;
    width: 28px;
    text-align: center;
    font-size: 7px;
    color: #fff;
  }
  .page--left .page-number { left: 2px; top: 608px; }
  .page--right .page-number { left: 454px; top: 608px; }
  .section-title {
    position: absolute;
    display: inline-block;
    border: 1.5px solid var(--teal-soft);
    color: var(--teal-soft);
    font-weight: 700;
    letter-spacing: 0.2px;
    line-height: 1;
  }
  .page--left .section-title { left: 45px; top: 45px; font-size: 21px; padding: 6px 8px; }
  .page--right .section-title { left: 26px; top: 36px; font-size: 16.5px; padding: 6px 7px; }
  .content {
    position: absolute;
    font-size: 6.9px;
    line-height: 10.3px;
    text-align: justify;
    overflow-wrap: break-word;
  }
  .page--left .content { left: 44px; top: 110px; width: 412px; }
  .page--right .content { left: 26px; top: 78px; width: 412px; }
  .sub-heading {
    display: flex;
    align-items: center;
    gap: 7px;
    font-size: 10.5px;
    font-weight: 700;
    color: var(--navy);
    margin-bottom: 10px;
  }
  .sub-heading__dot {
    width: 13px; height: 13px;
    border-radius: 50%;
    background: var(--teal);
    flex: none;
  }
  .intro-block + .intro-block { margin-top: 26px; }
  .scheme-heading {
    display: flex;
    align-items: center;
    gap: 7px;
    font-size: 11px;
    font-weight: 700;
    color: var(--navy);
    margin-bottom: 6px;
  }
  .scheme-heading__dot {
    width: 24px; height: 24px;
    border-radius: 50%;
    background: #6a2c7e;
    flex: none;
  }
  .content p + p { margin-top: 6px; }
  .service-list { list-style: none; margin-top: 7px; }
  .service-list li { margin-bottom: 8px; padding-left: 10px; position: relative; }
  .service-list li::before {
    content: "";
    position: absolute;
    left: 0; top: 3px;
    width: 5px; height: 5px;
    border-radius: 50%;
    background: var(--navy);
  }
  .service-list strong { font-weight: 700; color: var(--navy); display: block; }
  .photo {
    position: absolute;
    left: 72px; top: 401px;
    width: 410px; height: 212px;
    background: linear-gradient(160deg, #d7dbe0 0%, #a7adb6 45%, #6b6f79 100%);
  }
</style>
</head>
<body>

<section class="page page--left">
  <div class="photo" role="img" aria-label="Photo of a physiotherapist guiding an older woman through a floor balance exercise in a bright clinic gym"></div>
  <svg class="page-decor" viewBox="0 0 482 676" aria-hidden="true">
    <polygon points="0,450 20,450 290,676 260,676" fill="var(--teal-pale)"/>
    <polygon points="0,560 0,676 175,676" fill="var(--teal)" opacity="0.75"/>
    <polygon points="47,511 47,620 167,620" fill="var(--green)"/>
    <rect x="0" y="511" width="30" height="110" fill="var(--tab-grey)"/>
  </svg>
  <div class="page-frame"></div>
  <span class="page-number">4</span>

  <h1 class="section-title">INTRODUCTION</h1>

  <div class="content">
    <div class="intro-block">
      <h2 class="sub-heading"><span class="sub-heading__dot"></span>THE ‘YOU’ IN ‘COMMUNITY’</h2>
      <p>It’s no coincidence that the word ‘community’ contains the letters ‘y’, ‘o’ and ‘u’. Tidewell Care’s unique emphasis on community is founded on a commitment to help individuals of all ages to realise their personal best health and wellbeing, no matter what their injuries, disabilities or limitations. To us, the word ‘community’ means harnessing your personal strengths to enable your participation in a rich, rewarding, connected life. It means person-centred services and community engagement processes tailored to ensuring that clients with special needs receive the care they require and deserve, to realise their potential and enjoy optimal quality of life. It means a collaborative approach to treatment and partnering you on your journey. Tidewell Care community practitioners will support you to challenge your limitations and celebrate your progress as you gain confidence and accomplish things you didn’t believe you could.</p>
    </div>
    <div class="intro-block">
      <h2 class="sub-heading"><span class="sub-heading__dot"></span>WHAT SETS US APART</h2>
      <p>Since initially gaining national acclaim for helping athletes to reach their peak performance, Tidewell Care has earned a reputation for its unique, dedicated community focus. Led by director and senior chiropractor Dr Elias Varnell, who is passionate about each person’s right to know what it is to feel well and live their best life, our practice has become widely known among health practitioners and case managers as a caring, compassionate, specialised private practice with dedicated services and knowledge tailored to the special needs of clients with injuries, disabilities and chronic health conditions. We pride ourselves on upholding that reputation and exceeding the expectations of referrers and clients with a less-ordinary level of specialised care. From CSAS participants with severe disabilities to TIRS claimants recovering from life-altering accidents, our highly-trained, human-centred physiotherapists, chiropractors, occupational therapists, psychologists and dietitians meet each client where they are and support them to live rich, satisfying lives.</p>
    </div>
  </div>
</section>

<section class="page page--right">
  <svg class="page-decor" viewBox="0 0 482 676" aria-hidden="true">
    <polygon points="230,0 290,0 482,175 482,230" fill="var(--green-pale)"/>
    <polygon points="330,0 482,0 482,115" fill="var(--green-pale)" opacity="0.8"/>
    <rect x="454" y="511" width="28" height="120" fill="var(--tab-grey)"/>
  </svg>
  <div class="page-frame"></div>
  <span class="page-number">5</span>

  <h1 class="section-title">ACCEPTED SCHEMES AND PROGRAMS</h1>

  <div class="content">
    <h2 class="scheme-heading"><span class="scheme-heading__dot"></span>CSAS</h2>
    <p>If you’re living with a disability, you’re probably familiar with the challenges of accessing the help you need. Not only can the required frequency of therapy can make paying fees unaffordable, funding provisions and onerous application processes can further delay treatment. At Tidewell Care, we recognise the importance of accessing the therapeutic services you need, when you need them. As a registered CSAS provider, Tidewell Care’s practitioners treat eligible participants under the Community Support Access Scheme (CSAS). What’s more, our community coordinator and customer service team are well-versed in CSAS requirements and can help you to fast-track access to appropriate treatment.</p>
    <p><strong>CSAS services:</strong> As a registered CSAS provider, Tidewell Care provides our services to all local participants under the CSAS. Ways in which our therapists can help eligible CSAS participants to live well and thrive include:</p>
    <ul class="service-list">
      <li><strong>Realise your physical goals with your Tidewell Care physiotherapist:</strong>Whether you’re determined to achieve a certain functional goal, or look forward to relief from pain, swelling or stiffness, our experienced therapists can help. As well as using hands-on techniques, a Tidewell Care physiotherapist may plan a tailored exercise program and even hydrotherapy to help you reach your functional goals. Our physios can also help you with assistive technology, gait rehabilitation, neurological rehabilitation and postural devices.</li>
      <li><strong>Harness the healing power of food with your Tidewell Care dietitian:</strong>When it comes to realising your physical and mental potential, food is rarely given due credit. Not only can obtaining optimal quantities and combinations of nutrients assist with the body’s own repair processes, following tailored healthy eating recommendations from a Tidewell Care dietitian can restore a sense of vitality you may have thought you’d lost. If you’re looking to regain strength and muscle through exercise, strategic nutrition is also key to realising your goals.</li>
      <li><strong>Learn what it means to ‘live your best life’ with your Tidewell Care occupational therapist:</strong>With the right assistance, you may be surprised by quite how rich and fulfilling your life can be. Whether you’d like to find ways to independently manage daily living tasks or need help to realise an ambitious goal – from participating in adapted sports to travelling – a Tidewell Care occupational therapist can help make it happen. From recommending and helping to facilitate adaptations around the house (think bathroom rails and dressing aids), to advising on assistive and therapeutic technologies and devices such as specialised wheelchair tyres, the driving force behind the work your occupational therapist does is hearing you say the words, ‘I can’.</li>
      <li><strong>Feel the power of physical fitness and strength with yoga and Pilates:</strong>It may sound unlikely that small gains to flexibility, balance and coordination could lend a sense of empowerment and overall strength – but those who have experienced Pilates and yoga attest to the unique benefits of these physical practices. Even if it isn’t evident in fundamental physical function, devotees speak of feeling metaphorically ‘taller’ and ‘stronger’. Whether you have your yoga or Pilates technique down pat and feel able to practice in a group setting or need the one-on-one guidance and attention of private classes, Tidewell Care has a suitable program.</li>
      <li><strong>Maintain independent living with Tidewell Care domestic assistance and garden maintenance:</strong>Even if you are able to manage cleaning the house and other domestic tasks, the effort and time required to complete daily chores may leave you too tired or time-poor to enjoy a rich and full life doing what you want to do. That’s why we offer domestic assistance. Why not relieve some of the burden and let us help with tasks such as daily chores, cleaning and even grocery shopping? Our garden maintenance service can also assist with or take care of your gardening, so you can focus on living well, knowing your garden will also thrive.</li>
      <li><strong>Embrace the joy of sharing with Tidewell Care’s regular physical, recreational and social events:</strong>It can be hard to maintain social ties and activities when your mobility is limited – and sometimes you simply mightn’t feel like making small talk. But the mental health benefits of social interaction are backed by a host of evidence. Simply sharing experiences can foster a powerful sense of connectedness and relieve the sense of isolation and loneliness than can set in when interaction is limited. Let us know if you’re interested and we’ll let you know when we are planning a social event.</li>
    </ul>
  </div>
</section>

</body>
</html>
```